Exhibition Stand Design for innovative Social Business

We are an innovative social business empowering people to value nature through ZUN, a complementary digital currency. We have attached the TEK_ZUN branding document, and are needing a design for our exhibition stand (https://fairbuildlab.com/produit/stand-parapluie-classic-pvc-3x4c/. The attached doc mocks up a stand on page 32, though we would like some messaging included, in line with our website www.tekzun.ch. You will see there how the branding concept has been implemented with the Tek Grow, Share, Thrive wording, as well as Everyone wins. Our green colours are included in the branding document. Many thanks!

Industry/Entity Type

Environment

Font styles to use
Other font styles liked:
• As per our attached fonts

Requirements
Must have
• Our attached branding guidelines gives our look and feel - Innovative / Dynamic / Vibrant / Reliable / Accessible / Connected.

```html
<!DOCTYPE html>
<html lang="en">
<head>
<meta charset="utf-8">
<title>TekZun — Grow, Share, Thrive</title>
<link rel="stylesheet" href="https://fonts.googleapis.com/css2?family=Montserrat:wght@600;700&display=swap">
<style>
  :root {
    --green-cool: #46e8a2;
    --green-mid: #33ef6e;
    --green-vivid: #1ff03a;
    --white: #ffffff;
  }
  html, body {
    margin: 0;
    padding: 0;
    width: 1200px;
    height: 900px;
    overflow: hidden;
    background: var(--green-mid);
  }
  .stand-panel {
    display: block;
    width: 1200px;
    height: 900px;
    font-family: "Montserrat", sans-serif;
  }
  .headline { fill: var(--white); font-weight: 700; }
  .tagline { fill: var(--white); font-weight: 600; font-size: 34px; }
  .brand-name { fill: var(--white); font-weight: 600; font-size: 30px; }
  .ring { fill: none; stroke: var(--white); stroke-width: 1.5; }
</style>
</head>
<body>
<svg class="stand-panel" viewBox="0 0 1200 900" xmlns="http://www.w3.org/2000/svg">
  <defs>
    <linearGradient id="panel-bg" x1="0" y1="0" x2="1" y2="0">
      <stop offset="0" stop-color="#46e8a2"/>
      <stop offset="0.55" stop-color="#33ef6e"/>
      <stop offset="1" stop-color="#1ff03a"/>
    </linearGradient>
    <linearGradient id="cafe-tones" x1="0" y1="0" x2="1" y2="1">
      <stop offset="0" stop-color="#6b5040"/>
      <stop offset="0.45" stop-color="#d9c6b4"/>
      <stop offset="1" stop-color="#7a5a3e"/>
    </linearGradient>
    <linearGradient id="payment-tones" x1="0" y1="0" x2="1" y2="1">
      <stop offset="0" stop-color="#3a3530"/>
      <stop offset="0.5" stop-color="#c79a82"/>
      <stop offset="1" stop-color="#e8e2d8"/>
    </linearGradient>
    <linearGradient id="mountain-tones" x1="0" y1="0" x2="0" y2="1">
      <stop offset="0" stop-color="#cfd3cf"/>
      <stop offset="0.45" stop-color="#8d9693"/>
      <stop offset="1" stop-color="#2f3a2c"/>
    </linearGradient>
  </defs>

  <rect class="background" width="1200" height="900" fill="url(#panel-bg)"/>

  <g class="photo-circle photo-cafe">
    <circle cx="297" cy="196" r="228" fill="url(#cafe-tones)" role="img" aria-label="Photo of a smiling woman at a café table with a cup of coffee"/>
    <circle class="ring" cx="256" cy="196" r="239"/>
  </g>

  <g class="photo-circle photo-payment">
    <circle cx="1017" cy="496" r="254" fill="url(#payment-tones)" role="img" aria-label="Photo of a hand passing a payment card to another hand"/>
    <circle class="ring" cx="1011" cy="458" r="254"/>
  </g>

  <g class="photo-circle photo-hiker">
    <circle cx="200" cy="758" r="250" fill="url(#mountain-tones)" role="img" aria-label="Photo of a hiker with a yellow backpack looking over misty mountains"/>
    <circle class="ring" cx="221" cy="775" r="254"/>
  </g>

  <g class="headline-stack">
    <text class="headline" x="533" y="137" font-size="112">Tek</text>
    <text class="headline" x="450" y="323" font-size="160">Grow</text>
    <text class="headline" x="342" y="533" font-size="160">Share</text>
    <text class="headline" x="354" y="762" font-size="160">Thrive</text>
  </g>

  <text class="tagline" x="475" y="858">everyone wins</text>
  <text class="brand-name" x="1168" y="868" text-anchor="end">TekZun</text>
</svg>
</body>
</html>
```